Business Card for Web Design consulting firm

Business card designs for Web Design consulting firm

Target Market(s)

English speaking adults ages 30 - 60. Predominantly professional services eg. Doctor, Dentist

Industry/Entity Type

Consulting

Requirements
Must have
• Double sided card

```html
<!DOCTYPE html>
<html lang="en">
<head>
<meta charset="utf-8">
<title>Norvante Business Card – Front and Back</title>
<link rel="stylesheet" href="https://fonts.googleapis.com/css2?family=Lato:wght@400&display=swap">
<style>
  :root {
    --paper: #ffffff;
    --brand-orange: #f79a21;
    --ink-grey: #4a4a4a;
    --text-black: #1a1a1a;
  }
  * { margin: 0; padding: 0; box-sizing: border-box; }
  html, body {
    width: 1200px;
    height: 1200px;
    overflow: hidden;
    background: var(--paper);
  }
  .canvas {
    position: relative;
    width: 1200px;
    height: 1200px;
    font-family: "Lato", Arial, sans-serif;
  }
  .card {
    position: absolute;
    overflow: hidden;
  }
  .card--front {
    left: 99px;
    top: 120px;
    width: 768px;
    height: 480px;
    background: var(--paper);
    border: 1.5px solid var(--brand-orange);
  }
  .card--back {
    left: 305px;
    top: 645px;
    width: 766px;
    height: 477px;
    background: var(--brand-orange);
  }
  .brand {
    position: absolute;
    display: flex;
    align-items: center;
    gap: 18px;
    font-weight: 400;
    letter-spacing: 0.14em;
    color: var(--ink-grey);
    line-height: 1;
  }
  .brand__dot {
    flex: none;
    border-radius: 50%;
  }
  .card--front .brand {
    right: 54px;
    top: 118px;
    font-size: 58px;
  }
  .card--front .brand__dot {
    width: 34px;
    height: 34px;
    background: var(--brand-orange);
  }
  .card--back .brand {
    left: 0;
    right: 0;
    top: 196px;
    justify-content: center;
    font-size: 84px;
  }
  .card--back .brand__dot {
    width: 48px;
    height: 48px;
    background: var(--paper);
  }
  .contact {
    position: absolute;
    left: 48px;
    top: 290px;
    list-style: none;
    font-size: 24px;
    line-height: 34px;
    color: var(--text-black);
  }
</style>
</head>
<body>
  <main class="canvas">
    <section class="card card--front" aria-label="Card front">
      <div class="brand">
        <span class="brand__dot" aria-hidden="true"></span>
        <span class="brand__name">NORVANTE</span>
      </div>
      <ul class="contact">
        <li>Name goes here</li>
        <li>Job tile</li>
        <li>web Address</li>
        <li>email</li>
      </ul>
    </section>

    <section class="card card--back" aria-label="Card back">
      <div class="brand">
        <span class="brand__dot" aria-hidden="true"></span>
        <span class="brand__name">NORVANTE</span>
      </div>
    </section>
  </main>
</body>
</html>
```